I need a new business card design for my pharmacy.

I need a business card design. I will include my logo.
The card needs to be readable. I prefer to have my logo on one side along with my website, the other side includes the other information. Please use combination of black, neon green, white, and silver. This needs to catch the eye but yet be clearly visible and legible. Thanks

Industry/Entity Type

Pharmacy

Contact Information for Business Card

It needs to have the following information listed:
Vel's Apothecary Owner/Pharm D.
7143 North Birch Lane
Sioux Falls, SD 57362
Phone 605-318-6027
Fax 605-318-6025
email: vel@velsapothecary.example
www.velsapothecary.example
Store hours Monday-Friday 8 am- 7 pm
Saturday 8 am- 12 pm
Sunday Closed
Please utilize the colors black, white, and neon green, maybe silver.

Requirements
Must have
• It needs to be easily readable!
Nice to have
• It should catch the eye.
Should not have
• Do not use any other colors except listed: black, neon green, white, & silver.

```html
<!DOCTYPE html>
<html lang="en">
<head>
<meta charset="utf-8">
<title>Vel's Apothecary – Business Cards</title>
<link rel="stylesheet" href="https://fonts.googleapis.com/css2?family=Source+Sans+3:wght@400;600;700&display=swap">
<style>
  :root {
    --ink: #1f1f21;
    --ink-soft: #2b2b2d;
    --neon: #8dc63f;
    --neon-light: #b5dc5a;
    --neon-deep: #74b12d;
    --white: #ffffff;
    --silver: #d9d9d9;
    --silver-dark: #9a9a9a;
    --stage: #ebe8e3;
    --copy: #333335;
  }
  * { box-sizing: border-box; margin: 0; padding: 0; }
  html, body {
    width: 1200px; height: 950px; overflow: hidden;
    background: var(--stage);
    font-family: "Source Sans 3", "Helvetica Neue", Arial, sans-serif;
  }
  .card {
    position: absolute; top: 160px;
    width: 360px; height: 630px;
    border-radius: 4px;
    overflow: hidden;
    box-shadow: 0 10px 28px rgba(0,0,0,0.18);
  }

  /* ---------- Info side ---------- */
  .card--info { left: 210px; background: var(--ink); }
  .info-backdrop { position: absolute; inset: 0; }
  .contact {
    position: absolute; top: 40px; right: 30px;
    text-align: right; color: var(--silver);
    font-size: 16px; line-height: 1.32;
  }
  .contact__title { color: var(--neon); font-weight: 700; font-size: 24px; line-height: 1.1; }
  .contact__role { color: var(--white); font-size: 19px; margin-bottom: 8px; }
  .contact__label { color: var(--neon); font-weight: 700; }
  .contact__gap { height: 6px; }

  .info-name {
    position: absolute; top: 372px; left: 0; right: 0;
    display: flex; align-items: center; justify-content: center; gap: 12px;
    color: var(--ink); font-weight: 700; font-size: 34px;
  }
  .info-name__dot { width: 18px; height: 18px; border-radius: 50%; background: var(--white); }

  .hours {
    position: absolute; left: 26px; right: 26px; top: 456px;
    border-top: 1.5px solid var(--ink);
    border-bottom: 1.5px solid var(--ink);
    padding: 14px 0 14px 36px;
    color: var(--ink); font-size: 17px; line-height: 1.3;
  }
  .hours__tag {
    display: inline-block; background: var(--ink-soft); color: var(--silver);
    font-weight: 600; font-size: 16px; letter-spacing: 0.5px;
    padding: 1px 14px; margin: 2px 0 2px 26px;
  }
  .hours__tag--closed { margin-left: 0; }

  /* ---------- Brand side ---------- */
  .card--brand { left: 630px; background: var(--white); }
  .brand-panel {
    position: absolute; top: 0; left: 360px;
    width: 630px; height: 360px;
    transform-origin: 0 0; transform: rotate(90deg);
    padding: 70px 0 0 60px;
  }
  .brand-row { display: flex; align-items: center; gap: 22px; }
  .brand-mark { width: 54px; height: 54px; border-radius: 50%; background: var(--neon); }
  .brand-rule { width: 1.5px; height: 70px; background: var(--ink); }
  .brand-name { color: var(--ink); font-weight: 700; font-size: 44px; letter-spacing: -0.5px; }
  .values {
    margin: 14px 0 0 98px;
    display: flex; gap: 12px; align-items: center;
    color: var(--copy); font-size: 17px;
  }
  .values__item { display: flex; align-items: center; gap: 7px; }
  .values__item::before {
    content: ""; width: 6px; height: 6px; background: var(--neon);
  }
</style>
</head>
<body>

<section class="card card--info" aria-label="Contact and store hours side">
  <svg class="info-backdrop" viewBox="0 0 360 630" preserveAspectRatio="none" aria-hidden="true">
    <defs>
      <linearGradient id="neonFill" x1="0" y1="0" x2="0" y2="1">
        <stop offset="0" stop-color="#b5dc5a"/>
        <stop offset="1" stop-color="#8dc63f"/>
      </linearGradient>
    </defs>
    <rect width="360" height="630" fill="#1f1f21"/>
    <path d="M0 300 C 120 330, 240 350, 360 340 L360 630 L0 630 Z" fill="url(#neonFill)"/>
  </svg>

  <div class="contact">
    <p class="contact__title">Pharm D.</p>
    <p class="contact__role">Owner</p>
    <p>7143 North Birch Lane</p>
    <p>Sioux Falls, SD 57362</p>
    <div class="contact__gap"></div>
    <p><span class="contact__label">P :</span> 605-318-6027</p>
    <p><span class="contact__label">F :</span> 605-318-6025</p>
    <p>vel@velsapothecary.example</p>
    <p>www.velsapothecary.example</p>
  </div>

  <div class="info-name">
    <span class="info-name__dot"></span>
    <span>Vel's Apothecary</span>
  </div>

  <div class="hours">
    <p><span class="hours__tag">STORE HOURS</span></p>
    <p>Monday to Friday : 8 am - 7 pm</p>
    <p>Saturday : 8 am - 12 pm</p>
    <p><span class="hours__tag hours__tag--closed">Sunday Closed</span></p>
  </div>
</section>

<section class="card card--brand" aria-label="Brand side">
  <div class="brand-panel">
    <div class="brand-row">
      <span class="brand-mark"></span>
      <span class="brand-rule"></span>
      <span class="brand-name">Vel's Apothecary</span>
    </div>
    <div class="values">
      <span class="values__item">Accountability</span>
      <span class="values__item">Passion</span>
      <span class="values__item">Care</span>
      <span class="values__item">Respect</span>
    </div>
  </div>
</section>

</body>
</html>
```